KVT Calculator

We have a calculator already created however the design seems to be very boring and bland. The calculators goal is to show graphic designers, web development firms, pr agencies, marketing firms how much revenue they can potentially make by offering a managed social media solution to their clients.

We want a great designer to make the calculator appealing to our audience.

It is an amazing offer and opportunity however I do not believe the current design does it justice

you can view and play with calculator live at http://sandbox.plivoran.com/tkna/

```html
<!DOCTYPE html>
<html lang="en">
<head>
<meta charset="utf-8">
<title>Profit Calculator</title>
<link href="https://fonts.googleapis.com/css2?family=Open+Sans:wght@400;600;700&display=swap" rel="stylesheet">
<style>
  :root {
    --backdrop: #8a5530;
    --frame: #b4b7c0;
    --table-dark: #333333;
    --card: #ffffff;
    --cell: #f7f7f7;
    --rule: #cfcfcf;
    --ink: #444444;
    --ink-strong: #333333;
    --blue-top: #3550a8;
    --blue-bottom: #1f3580;
    --orange-top: #ff9500;
    --orange-bottom: #ff5200;
    --button-dark: #1c1c1c;
  }
  * { margin: 0; padding: 0; box-sizing: border-box; }
  html, body { width: 1200px; height: 824px; overflow: hidden; }
  body {
    position: relative;
    background: var(--backdrop);
    font-family: "Open Sans", Arial, sans-serif;
    color: var(--ink);
  }
  .calculator {
    position: absolute; left: 47px; top: 135px; width: 1095px; height: 518px;
    background: var(--frame);
  }
  .table-backing {
    position: absolute; left: 63px; top: 40px; width: 975px; height: 330px;
    background: var(--table-dark);
    box-shadow: 0 6px 10px rgba(0,0,0,.35);
  }
  .term-card {
    position: absolute; left: 73px; top: 21px; width: 165px; height: 464px;
    background: var(--card);
    box-shadow: 0 3px 4px rgba(0,0,0,.25);
  }
  .term-label {
    position: absolute; left: 7px; top: 10px; width: 153px; height: 42px;
    background: linear-gradient(#3a3a3a, var(--button-dark));
    border-radius: 3px;
    color: #fff; font-weight: 600; font-size: 17px;
    display: flex; align-items: center; justify-content: center;
  }
  .term-slider { position: absolute; left: 0; top: 0; }
  .row-label {
    position: absolute; left: 247px; width: 210px;
    color: #fff; font-weight: 700; font-size: 16px; line-height: 22px;
  }
  .row-rule {
    position: absolute; left: 243px; width: 213px; height: 1px; background: #555;
  }
  .plan {
    position: absolute; top: 20px; width: 176px; height: 357px;
    background: var(--card); border-radius: 4px;
    box-shadow: 0 2px 5px rgba(0,0,0,.3);
    overflow: hidden;
  }
  .plan--basic { left: 466px; }
  .plan--pro { left: 658px; width: 175px; }
  .plan--enterprise { left: 848px; }
  .plan-title {
    position: absolute; left: 4px; right: 4px; top: 4px; height: 58px;
    border-radius: 3px;
    color: #fff; font-size: 21px; font-weight: 600;
    display: flex; align-items: center; justify-content: center;
    background: linear-gradient(var(--blue-top), var(--blue-bottom));
  }
  .plan--pro .plan-title { background: linear-gradient(var(--orange-top), var(--orange-bottom)); }
  .plan-cell {
    position: absolute; left: 0; right: 0; height: 70px;
    background: var(--cell); border-top: 1px solid var(--rule);
    display: flex; align-items: center; justify-content: center;
    font-size: 21px; font-weight: 600; color: var(--ink);
  }
  .plan-cell--clients { top: 62px; height: 70px; background: var(--card); border-top: none; }
  .plan-cell--cost { top: 132px; }
  .plan-cell--price { top: 202px; }
  .plan-cell--profit { top: 273px; height: 62px; padding-top: 14px; font-weight: 700; font-size: 18px; color: var(--ink-strong); }
  .stepper {
    position: absolute; top: 50%; margin-top: -14px;
    width: 28px; height: 28px; border-radius: 50%;
    background: linear-gradient(#f2f2f2, #cfcfcf);
    border: 1px solid #b8b8b8;
  }
  .stepper--minus { left: 4px; }
  .stepper--plus { right: 4px; }
  .stepper::before, .stepper--plus::after {
    content: ""; position: absolute; left: 7px; top: 12px; width: 12px; height: 3px; background: #333;
  }
  .stepper--plus::after { left: 12px; top: 7px; width: 3px; height: 12px; }
  .plan-bar {
    position: absolute; left: 4px; right: 4px; top: 335px; height: 14px;
    background: linear-gradient(var(--blue-top), var(--blue-bottom));
  }
  .plan--pro .plan-bar { background: linear-gradient(#ffc400, var(--orange-bottom)); }
  .summary {
    position: absolute; left: 256px; top: 406px; width: 782px; height: 78px;
    background: linear-gradient(#ffffff, #e6e6e8);
    box-shadow: 0 3px 4px rgba(0,0,0,.25);
    display: flex; align-items: center; justify-content: center;
    font-size: 33px; color: var(--ink-strong);
  }
  .summary strong { font-weight: 700; margin-left: 10px; }
</style>
</head>
<body>
  <main class="calculator">
    <div class="table-backing"></div>

    <section class="term-card">
      <div class="term-label">TERM (YRS)</div>
      <svg class="term-slider" width="165" height="464" viewBox="0 0 165 464" aria-label="Term slider">
        <g stroke="#d6d6d6" stroke-width="1">
          <line x1="55" x2="100" y1="114" y2="114"/><line x1="55" x2="100" y1="184" y2="184"/>
          <line x1="55" x2="100" y1="218" y2="218"/><line x1="55" x2="100" y1="252" y2="252"/>
          <line x1="55" x2="100" y1="286" y2="286"/><line x1="55" x2="100" y1="320" y2="320"/>
          <line x1="55" x2="100" y1="354" y2="354"/><line x1="55" x2="100" y1="389" y2="389"/>
        </g>
        <defs>
          <linearGradient id="trackFill" x1="0" x2="1">
            <stop offset="0" stop-color="#2a3f95"/><stop offset=".5" stop-color="#4860bf"/><stop offset="1" stop-color="#2a3f95"/>
          </linearGradient>
        </defs>
        <rect x="69" y="98" width="17" height="314" rx="7" fill="url(#trackFill)" stroke="#1a2450"/>
        <path d="M69 105a7 7 0 0 1 7-7h3a7 7 0 0 1 7 7v43h-17z" fill="#0e3550"/>
        <circle cx="77" cy="148" r="20" fill="#ffffff" stroke="#cccccc"/>
        <circle cx="77" cy="148" r="9" fill="#aaaaaa" stroke="#777777"/>
      </svg>
    </section>

    <div class="row-label" style="top:107px">Clients per month:</div>
    <div class="row-rule" style="top:150px"></div>
    <div class="row-label" style="top:177px">Your cost:</div>
    <div class="row-rule" style="top:221px"></div>
    <div class="row-label" style="top:247px">Your client pays:</div>
    <div class="row-rule" style="top:292px"></div>
    <div class="row-label" style="top:321px">Monthly profit (year 8):</div>

    <section class="plan plan--basic">
      <div class="plan-cell plan-cell--clients"><span class="stepper stepper--minus"></span>1<span class="stepper stepper--plus"></span></div>
      <div class="plan-title">BASIC</div>
      <div class="plan-cell plan-cell--cost">$197</div>
      <div class="plan-cell plan-cell--price"><span class="stepper stepper--minus"></span>$297<span class="stepper stepper--plus"></span></div>
      <div class="plan-cell plan-cell--profit">$9,600</div>
      <div class="plan-bar"></div>
    </section>

    <section class="plan plan--pro">
      <div class="plan-cell plan-cell--clients"><span class="stepper stepper--minus"></span>1<span class="stepper stepper--plus"></span></div>
      <div class="plan-title">PRO</div>
      <div class="plan-cell plan-cell--cost">$297</div>
      <div class="plan-cell plan-cell--price"><span class="stepper stepper--minus"></span>$497<span class="stepper stepper--plus"></span></div>
      <div class="plan-cell plan-cell--profit">$19,200</div>
      <div class="plan-bar"></div>
    </section>

    <section class="plan plan--enterprise">
      <div class="plan-cell plan-cell--clients"><span class="stepper stepper--minus"></span>1<span class="stepper stepper--plus"></span></div>
      <div class="plan-title">ENTERPRISE</div>
      <div class="plan-cell plan-cell--cost">$2500</div>
      <div class="plan-cell plan-cell--price"><span class="stepper stepper--minus"></span>$4000<span class="stepper stepper--plus"></span></div>
      <div class="plan-cell plan-cell--profit">$144,000</div>
      <div class="plan-bar"></div>
    </section>

    <div class="summary">Monthly profit by the end of year 8: <strong>$172,800</strong></div>
  </main>
</body>
</html>
```